Mining Engineer Needs a Personal Design

Hi.

I would like a business card designed which includes a logo design. I would like it to be simple. Neat and tidy. I need this to go to print by Friday 1st August. The colours I would like you to use are black, royal blue and white. My initials TBH can be used to base this design on or my full name Troy Bell Hartley. The design should have one side with just the logo and one side with the logo and all my details below.

Troy Bell Hartley
Mining Engineer
M: +61 417 293 518
E: quarryhand@fernmail.example
Q: BEng (Mining Engineer), BComm (Management), RTQPA.

Industry/Entity Type

Business

```html
<!DOCTYPE html>
<html lang="en">
<head>
<meta charset="utf-8">
<title>Troy Bell Hartley — Business Card</title>
<link rel="stylesheet" href="https://fonts.googleapis.com/css2?family=Roboto+Slab:wght@400;700;800&display=swap">
<style>
  :root {
    --royal: #2b3fd4;
    --royal-pale: #dfe3f7;
    --ink: #1c1c1c;
    --paper: #ffffff;
    --backdrop: #e9e9eb;
    --shadow: rgba(0, 0, 0, 0.18);
  }
  * { margin: 0; padding: 0; box-sizing: border-box; }
  html, body { width: 1200px; height: 873px; overflow: hidden; }
  body {
    background: var(--backdrop);
    font-family: "Roboto Slab", Georgia, serif;
    color: var(--ink);
    display: flex;
    align-items: center;
    justify-content: center;
    gap: 60px;
  }
  .card {
    position: relative;
    width: 520px;
    height: 300px;
    background: var(--paper);
    box-shadow: 0 10px 28px var(--shadow);
    overflow: hidden;
  }
  .band {
    position: absolute;
    left: 0;
    width: 100%;
    height: 38px;
    background: linear-gradient(90deg, var(--royal) 0%, var(--royal) 30%, var(--royal-pale) 100%);
    display: flex;
    align-items: center;
    padding-left: 26px;
    color: var(--paper);
    font-weight: 700;
    font-size: 17px;
    letter-spacing: 0.2px;
  }
  .wordmark {
    position: absolute;
    color: var(--royal);
    font-weight: 800;
    line-height: 1;
    letter-spacing: -2px;
  }

  /* Details side */
  .card--details .wordmark { right: 34px; top: 34px; font-size: 64px; }
  .card--details .band { top: 118px; }
  .details {
    position: absolute;
    left: 26px;
    top: 168px;
    list-style: none;
    font-size: 13.5px;
    line-height: 1.55;
  }
  .details .label {
    display: inline-block;
    width: 20px;
    color: var(--royal);
    font-weight: 700;
  }
  .details .indent { padding-left: 20px; }

  /* Logo side */
  .card--logo .wordmark { right: 40px; top: 50px; font-size: 118px; letter-spacing: -4px; }
  .card--logo .band { top: 214px; font-size: 18px; }
</style>
</head>
<body>
  <section class="card card--details" aria-label="Business card, details side">
    <div class="wordmark">TBH</div>
    <div class="band">Troy Bell Hartley</div>
    <ul class="details">
      <li class="indent">Mining Engineer</li>
      <li><span class="label">M</span>+61 417 293 518</li>
      <li><span class="label">E</span>quarryhand@fernmail.example</li>
      <li><span class="label">Q</span>BEng (Mining Engineer),</li>
      <li class="indent">BComm (Management), RTQPA.</li>
    </ul>
  </section>

  <section class="card card--logo" aria-label="Business card, logo side">
    <div class="wordmark">TBH</div>
    <div class="band">Mining Engineer</div>
  </section>
</body>
</html>
```